A WEBSITE FOR A JEWELLERY RETAIL STORE WITH A SHOPPING CART, AND ABILITY TO ORDER ONLINE.

I require a website with a shopping cart.

We sell MAINLY diamond jewellery (such as rings etc). I need it to be simple to change prices with only a few buttons, as the price fluctuates due to the US Dollar.

We are a diamond wholesaler, selling directly to the public, so we guarantee the lowest prices in Australia.

There is also a link to current inventory that will need to be uploaded to the site.

This could be an ongoing job, where you will be paid weekly to maintain and update the website if you wish.

Target Market(s)

People getting engaged, and wanting to buy a diamond ring.

Number of Pages Required

5+ page

Colors

Designer to choose colors to be used in the design.

Requirements
Must have
• elegant.
• modern.
• professional.
• SHOPPING CART.
• ABILITY TO SEARCH FOR LOOSE DIAMONDS (LINK THAT NEEDS TO BE EMBEDDED WILL BE SENT WHICH SHOWS CURRENT STOCK).
• ENGAGEMENT RINGS
• WEDDING RINGS
• DIAMOND EARRINGS
• DIAMOND PENDANTS
• LOOSE DIAMONDS.
• SALE ITEMS.
• OTHER JEWELLERY.
• EDUCATION
• WISH LIST
• CART.
Nice to have
• a good place to look for inspiration on pages is https://www.lumenvael.example.
• YOU MAY VISIT OUR FRIENDSY PAGE AT.
• HTTP://WWW.SOCIALPAGE.EXAMPLE/QUILLSTONEJEWELLERS
Should not have
• We don't want it too busy.

```html
<!DOCTYPE html>
<html lang="en">
<head>
<meta charset="utf-8">
<title>Quillstone Jewellers Australia – Engagement Rings</title>
<link rel="stylesheet" href="https://fonts.googleapis.com/css2?family=Questrial&family=Cormorant+Garamond:wght@400;500&family=Montserrat:wght@600&display=swap">
<style>
:root{
  --ink:#111;
  --black:#000;
  --white:#fff;
  --grey:#555;
  --line:#c9c9c9;
  --accent:#9b2a22;
  --maroon:#3b1410;
  --band:#8b7866;
  --skin-a:#e9c3ad;
  --skin-b:#b9866a;
  --metal-a:#f4f4f6;
  --metal-b:#b8bcc4;
  --gold-a:#f7f0d8;
  --gold-b:#d8c37c;
}
*{box-sizing:border-box;margin:0;padding:0}
html,body{width:1200px;height:2811px;overflow:hidden;background:var(--white)}
body{position:relative;font-family:"Questrial",sans-serif;color:var(--ink)}
.abs{position:absolute}

.promo-bar{left:0;top:0;width:1200px;height:62px;background:var(--black);color:var(--white);
  display:flex;align-items:center;justify-content:center;font-family:"Cormorant Garamond",serif;font-size:16px;letter-spacing:1.2px}

.country{left:26px;top:112px;font-size:14px;letter-spacing:1.5px;display:flex;align-items:center;gap:6px}
.country-select{border:1px solid #999;border-radius:6px;padding:2px 8px;font-size:13px;display:flex;gap:14px}
.brand{left:445px;top:94px;width:300px;text-align:center}
.brand-name{font-size:23px;letter-spacing:1px;white-space:nowrap;display:flex;justify-content:center;align-items:center;gap:8px;height:34px}
.brand-mark{width:11px;height:11px;background:var(--ink);flex:none}
.brand-rule{height:3px;background:var(--maroon);margin:8px 10px 0}
.brand-region{font-family:"Cormorant Garamond",serif;font-size:13px;letter-spacing:9px;margin-top:7px}
.account-links{top:115px;font-size:14px;letter-spacing:1.3px;white-space:nowrap}
.header-rule{left:0;top:210px;width:1200px;height:1px;background:var(--line)}
.nav-rule{left:0;top:300px;width:1200px;height:1px;background:var(--line)}
.nav-item{top:237px;font-size:13px;letter-spacing:2.5px;white-space:nowrap}
.search{left:897px;top:234px;width:252px;border-bottom:1px solid #999;font-size:11px;letter-spacing:1.5px;color:var(--grey);padding-bottom:3px}
.search svg{position:absolute;right:8px;top:-4px}

.breadcrumb{left:44px;top:340px;font-size:13.5px;letter-spacing:.8px}
.breadcrumb .current{color:var(--accent)}

.hero-photo{left:46px;top:389px;width:1116px;height:422px;
  background:linear-gradient(110deg,#f1d7c6 0%,var(--skin-a) 35%,var(--skin-b) 70%,#7e5d4c 100%)}
.hero-frame-right{left:1135px;top:389px;width:27px;height:422px;background:var(--black)}
.hero-frame-bottom{left:982px;top:772px;width:180px;height:39px;background:var(--black)}
.hero-card{left:551px;top:420px;width:584px;height:352px;background:var(--white);padding:36px 36px 0 38px}
.hero-title{font-family:"Cormorant Garamond",serif;font-weight:400;font-size:20px;letter-spacing:1.5px;text-align:center;padding-bottom:4px;border-bottom:1px solid #888;margin:0 0 20px}
.hero-copy{font-size:14px;line-height:15.9px;letter-spacing:1px;text-align:justify;color:#333;padding:0 6px}

.filter-title{left:66px;font-family:"Cormorant Garamond",serif;font-size:15px;letter-spacing:1.5px;color:#444}
.filter-chevron{left:297px}
.filter-option{left:66px;font-size:10px;letter-spacing:1px;color:#444;display:flex;align-items:center;gap:9px;white-space:nowrap}
.filter-option::before{content:"";width:8px;height:8px;border:1.5px solid #333}

.toolbar{left:380px;width:775px;font-size:17px;letter-spacing:1.4px;color:#333;display:flex;justify-content:space-between}
.toolbar .sort{display:flex;gap:8px;align-items:center}

.product{width:260px;text-align:center}
.product-photo{width:176px;height:142px;margin:0 auto;border-radius:50% 50% 12px 12px}
.photo-white{background:radial-gradient(circle at 50% 35%,var(--metal-a) 0%,#dfe3ea 45%,var(--metal-b) 100%)}
.photo-gold{background:radial-gradient(circle at 50% 35%,var(--metal-a) 0%,var(--gold-a) 45%,var(--gold-b) 100%)}
.product-name{margin-top:23px;font-size:9.5px;letter-spacing:.7px;line-height:12px;color:#555}
.product-price{margin-top:4px;font-family:"Montserrat",sans-serif;font-size:9px;letter-spacing:1.2px}
.add-to-cart{display:block;width:146px;height:47px;margin:9px auto 0;border:2px solid var(--ink);background:var(--white);
  font-family:"Questrial",sans-serif;font-size:14px;letter-spacing:2px;color:var(--ink)}
.sale-badge{left:907px;top:1640px;width:92px;height:92px;border-radius:50%;background:var(--maroon);color:var(--white);
  font-family:"Montserrat",sans-serif;font-size:19px;letter-spacing:2px;line-height:22px;display:flex;align-items:center;justify-content:center;text-align:center}

.newsletter{left:0;top:2444px;width:1200px;height:79px;background:var(--band);color:var(--white)}
.newsletter-title{left:47px;top:29px;font-family:"Cormorant Garamond",serif;font-size:19px;letter-spacing:2.5px;white-space:nowrap}
.newsletter-input{left:237px;top:20px;width:263px;height:36px;background:var(--white);color:#888;font-size:13px;letter-spacing:1px;padding:9px 7px;white-space:nowrap;overflow:hidden}
.newsletter-button{left:500px;top:20px;width:132px;height:36px;background:var(--black);color:var(--white);font-size:12px;letter-spacing:1.5px;display:flex;align-items:center;justify-content:center}
.social-title{left:723px;top:29px;font-family:"Cormorant Garamond",serif;font-size:19px;letter-spacing:2.5px;white-space:nowrap}
.social-link{top:31px;font-size:13px;letter-spacing:.5px;display:flex;align-items:center;gap:5px;white-space:nowrap}
.social-link::before{content:"";width:9px;height:9px;border-radius:50%;background:var(--white)}

.footer{left:0;top:2523px;width:1200px;height:288px;background:var(--black);color:var(--white)}
.footer-about{left:48px;top:40px;width:300px;font-size:14px;line-height:16px;letter-spacing:.8px;text-align:justify}
.footer-help{left:49px;top:200px;font-size:10px;letter-spacing:.8px}
.footer-contact{left:60px;font-size:10px;letter-spacing:.8px;display:flex;gap:6px;align-items:center;white-space:nowrap}
.footer-col{top:38px;font-size:13px;letter-spacing:1.3px;line-height:26px;white-space:nowrap}
.footer-col h3{font-weight:400;font-size:15px;text-decoration:underline;margin-bottom:3px}
.copyright{left:0;top:238px;width:1200px;text-align:center;font-size:12px;letter-spacing:1.2px}
</style>
</head>
<body>

<div class="abs promo-bar">ORDER NOW AND ENJOY FREE SWIFTPARCEL OVERNIGHT SHIPPING AND 30-DAY RETURNS</div>

<div class="abs country">Select your country: <span class="country-select">$AUD <span>▾</span></span></div>

<div class="abs brand">
  <div class="brand-name"><span class="brand-mark"></span>QUILLSTONE JEWELLERS</div>
  <div class="brand-rule"></div>
  <div class="brand-region">AUSTRALIA</div>
</div>

<div class="abs account-links" style="left:831px">Register | Sign In</div>
<div class="abs account-links" style="left:984px">Wishlist ♥</div>
<div class="abs account-links" style="left:1081px">Cart (0)</div>

<div class="abs header-rule"></div>
<nav>
  <span class="abs nav-item" style="left:46px">DIAMONDS</span>
  <span class="abs nav-item" style="left:183px">ENGAGEMENT RINGS</span>
  <span class="abs nav-item" style="left:404px">WEDDING</span>
  <span class="abs nav-item" style="left:524px">JEWELRY</span>
  <span class="abs nav-item" style="left:650px">EDUCATION</span>
  <span class="abs nav-item" style="left:788px">ON SALE</span>
  <div class="abs search">Search
    <svg width="18" height="14" viewBox="0 0 18 14"><circle cx="6" cy="6" r="4.5" fill="none" stroke="#555" stroke-width="1.4"/><line x1="9.5" y1="9" x2="16" y2="12.5" stroke="#555" stroke-width="1.6"/></svg>
  </div>
</nav>
<div class="abs nav-rule"></div>

<div class="abs breadcrumb">Home &gt;&gt; Jewellery &gt;&gt; Rings &gt;&gt; <span class="current">Engagement Rings</span></div>

<div class="abs hero-photo" role="img" aria-label="Close-up of a couple's hands wearing an engagement ring and a gold wedding band"></div>
<div class="abs hero-frame-right"></div>
<div class="abs hero-frame-bottom"></div>
<section class="abs hero-card">
  <h1 class="hero-title">ENGAGEMENT RINGS</h1>
  <p class="hero-copy">Lorem ipsum dolor sit amet, consectetur adipisicing elit, sed do eiusmod tempor incididunt ut labore et dolore magna aliqua. Ut enim ad minim veniam, quis nostrud exercitation ullamco laboris nisi ut aliquip ex ea commodo consequat. Duis aute irure dolor in reprehenderit in voluptate velit esse cillum dolore eu fugiat nulla pariatur. Excepteur sint occaecat cupidatat non proident, sunt in culpa qui officia deserunt mollit anim id est laborum. Sed ut perspiciatis unde omnis iste natus error sit voluptatem accusantium doloremque laudantium, totam rem aperiam, eaque ipsa quae ab illo inventore veritatis et quasi architecto beatae vitae dicta sunt explicabo. Nemo enim ipsam voluptatem quia voluptas sit aspernatur aut odit aut fugit, sed quia consequuntur magni dolores eos qui ratione voluptatem sequi nesciunt. Neque porro quisquam est, qui dolorem ipsum quia dolor sit amet, consectetur, adipisci velit, sed</p>
</section>

<aside>
  <div class="abs filter-title" style="top:926px">PRICE</div><div class="abs filter-chevron" style="top:926px">∨</div>
  <div class="abs filter-option" style="top:954px">AUD XXX - AUD XXX (YY)</div>
  <div class="abs filter-option" style="top:974px">AUD XXX - AUD XXX (YY)</div>
  <div class="abs filter-option" style="top:993px">AUD XXX - AUD XXX (YY)</div>
  <div class="abs filter-option" style="top:1013px">AUD XXX - AUD XXX (YY)</div>

  <div class="abs filter-title" style="top:1068px">PRODUCT TYPE</div><div class="abs filter-chevron" style="top:1068px">∨</div>
  <div class="abs filter-option" style="top:1096px">Rings (XXX)</div>

  <div class="abs filter-title" style="top:1152px">RECIPIENT</div><div class="abs filter-chevron" style="top:1152px">∨</div>
  <div class="abs filter-option" style="top:1180px">For Her (XXX)</div>
  <div class="abs filter-option" style="top:1197px">For Him (XXX)</div>

  <div class="abs filter-title" style="top:1249px">BRAND</div><div class="abs filter-chevron" style="top:1249px">∨</div>
  <div class="abs filter-option" style="top:1276px">Brand name 1 (XXX)</div>
  <div class="abs filter-option" style="top:1293px">Brand name 2 (XXX)</div>

  <div class="abs filter-title" style="top:1359px">RING STYLE</div><div class="abs filter-chevron" style="top:1359px">∨</div>
  <div class="abs filter-option" style="top:1387px">Cluster Engagement Rings (XXX)</div>
  <div class="abs filter-option" style="top:1405px">Engagement Rings (XXX)</div>
  <div class="abs filter-option" style="top:1422px">Eternity Rings (XXX)</div>
  <div class="abs filter-option" style="top:1440px">Solitaire Engagement Rings (XXX)</div>
  <div class="abs filter-option" style="top:1458px">Halo Engagement Rings (XXX)</div>

  <div class="abs filter-title" style="top:1525px">GEMSTONE SHAPE</div><div class="abs filter-chevron" style="top:1525px">∨</div>
  <div class="abs filter-option" style="top:1553px">Emerald Cut (XXX)</div>
  <div class="abs filter-option" style="top:1570px">Oval Cut (XXX)</div>
  <div class="abs filter-option" style="top:1588px">Princess Cut (XXX)</div>
  <div class="abs filter-option" style="top:1605px">Round Brilliant Cut (XXX)</div>

  <div class="abs filter-title" style="top:1676px">MATERIAL</div><div class="abs filter-chevron" style="top:1676px">∨</div>
  <div class="abs filter-option" style="top:1703px">18ct White Gold (XXX)</div>
  <div class="abs filter-option" style="top:1721px">18ct Yellow Gold (XXX)</div>
  <div class="abs filter-option" style="top:1738px">Platinum (XXX)</div>
</aside>

<div class="abs toolbar" style="top:922px"><span>xxx Products &nbsp;|&nbsp; Show &nbsp;00 22 33</span><span>1/16</span><span class="sort">Sort By:Recommended <small>▾</small></span></div>

<main>
  <div class="abs product" style="left:370px;top:1020px"><div class="product-photo photo-white" role="img" aria-label="Marquise diamond halo ring in white gold"></div><p class="product-name">Lorem ipsum dolor sit amet,<br>consectetur adipisicing elit, sed do</p><p class="product-price">AUD XXXX.XX</p><button class="add-to-cart">ADD TO CART</button></div>
  <div class="abs product" style="left:636px;top:1020px"><div class="product-photo photo-white" role="img" aria-label="Round diamond split-shank ring in white gold"></div><p class="product-name">Lorem ipsum dolor sit amet,<br>consectetur adipisicing elit, sed do</p><p class="product-price">AUD XXXX.XX</p><button class="add-to-cart">ADD TO CART</button></div>
  <div class="abs product" style="left:917px;top:1020px"><div class="product-photo photo-gold" role="img" aria-label="Round diamond halo ring in yellow gold"></div><p class="product-name">Lorem ipsum dolor sit amet,<br>consectetur adipisicing elit, sed do</p><p class="product-price">AUD XXXX.XX</p><button class="add-to-cart">ADD TO CART</button></div>

  <div class="abs product" style="left:370px;top:1336px"><div class="product-photo photo-white" role="img" aria-label="Marquise diamond halo ring in white gold"></div><p class="product-name">Lorem ipsum dolor sit amet,<br>consectetur adipisicing elit, sed do</p><p class="product-price">AUD XXXX.XX</p><button class="add-to-cart">ADD TO CART</button></div>
  <div class="abs product" style="left:636px;top:1336px"><div class="product-photo photo-white" role="img" aria-label="Round diamond split-shank ring in white gold"></div><p class="product-name">Lorem ipsum dolor sit amet,<br>consectetur adipisicing elit, sed do</p><p class="product-price">AUD XXXX.XX</p><button class="add-to-cart">ADD TO CART</button></div>
  <div class="abs product" style="left:917px;top:1336px"><div class="product-photo photo-gold" role="img" aria-label="Round diamond halo ring in yellow gold"></div><p class="product-name">Lorem ipsum dolor sit amet,<br>consectetur adipisicing elit, sed do</p><p class="product-price">AUD XXXX.XX</p><button class="add-to-cart">ADD TO CART</button></div>

  <div class="abs product" style="left:370px;top:1691px"><div class="product-photo photo-white" role="img" aria-label="Marquise diamond halo ring in white gold"></div><p class="product-name">Lorem ipsum dolor sit amet,<br>consectetur adipisicing elit, sed do</p><p class="product-price">AUD XXXX.XX</p><button class="add-to-cart">ADD TO CART</button></div>
  <div class="abs product" style="left:636px;top:1691px"><div class="product-photo photo-white" role="img" aria-label="Round diamond split-shank ring in white gold"></div><p class="product-name">Lorem ipsum dolor sit amet,<br>consectetur adipisicing elit, sed do</p><p class="product-price">AUD XXXX.XX</p><button class="add-to-cart">ADD TO CART</button></div>
  <div class="abs product" style="left:917px;top:1691px"><div class="product-photo photo-gold" role="img" aria-label="Round diamond halo ring in yellow gold"></div><p class="product-name">Lorem ipsum dolor sit amet,<br>consectetur adipisicing elit, sed do</p><p class="product-price">AUD XXXX.XX</p><button class="add-to-cart">ADD TO CART</button></div>
  <div class="abs sale-badge">ON<br>SALE</div>

  <div class="abs product" style="left:370px;top:2035px"><div class="product-photo photo-white" role="img" aria-label="Marquise diamond halo ring in white gold"></div><p class="product-name">Lorem ipsum dolor sit amet,<br>consectetur adipisicing elit, sed do</p><p class="product-price">AUD XXXX.XX</p><button class="add-to-cart">ADD TO CART</button></div>
  <div class="abs product" style="left:636px;top:2035px"><div class="product-photo photo-white" role="img" aria-label="Round diamond split-shank ring in white gold"></div><p class="product-name">Lorem ipsum dolor sit amet,<br>consectetur adipisicing elit, sed do</p><p class="product-price">AUD XXXX.XX</p><button class="add-to-cart">ADD TO CART</button></div>
  <div class="abs product" style="left:917px;top:2035px"><div class="product-photo photo-gold" role="img" aria-label="Round diamond halo ring in yellow gold"></div><p class="product-name">Lorem ipsum dolor sit amet,<br>consectetur adipisicing elit, sed do</p><p class="product-price">AUD XXXX.XX</p><button class="add-to-cart">ADD TO CART</button></div>
</main>

<div class="abs toolbar" style="top:2384px"><span>xxx Products &nbsp;|&nbsp; Show &nbsp;00 22 33</span><span>1/16</span><span class="sort">Sort By:Recommended <small>▾</small></span></div>

<section class="abs newsletter">
  <div class="abs newsletter-title">STAY IN TOUCH</div>
  <div class="abs newsletter-input">Please enter your email address</div>
  <div class="abs newsletter-button">SIGN UP</div>
  <div class="abs social-title">OUR SOCIAL SIDE</div>
  <span class="abs social-link" style="left:935px">Friendsy</span>
  <span class="abs social-link" style="left:1010px">Snapgram</span>
  <span class="abs social-link" style="left:1098px">Chirper</span>
</section>

<footer class="abs footer">
  <p class="abs footer-about">Lorem ipsum dolor sit amet, consectetur adipisicing elit, sed do eiusmod tempor incididunt ut labore et dolore magna aliqua. Ut enim ad minim veniam, quis nostrud exercitation ullamco laboris nisi ut aliquip ex ea commodo consequat. Duis aute irure dolor in reprehenderit in voluptate velit esse cillum dolore eu fugiat nulla pariatur. Excepteur sint occaecat</p>
  <div class="abs footer-help">Need Help?</div>
  <div class="abs footer-contact" style="top:224px">
    <svg width="8" height="8" viewBox="0 0 8 8"><path d="M1 1 L3 1 L3.6 2.8 L2.6 3.6 Q3.6 5 4.6 5.6 L5.4 4.6 L7 5.2 L7 7 Q3 7 1 1Z" fill="#fff"/></svg>+61-000-555-0188</div>
  <div class="abs footer-contact" style="top:242px">
    <svg width="8" height="6" viewBox="0 0 8 6"><rect x=".5" y=".5" width="7" height="5" fill="none" stroke="#fff"/><path d="M.5 .5 L4 3.5 L7.5 .5" fill="none" stroke="#fff"/></svg>hello@quillstone.example</div>
  <div class="abs footer-col" style="left:578px"><h3>Account</h3>Sign up for an account<br>Terms and Conditions<br>Privacy Policy<br>Site Map</div>
  <div class="abs footer-col" style="left:790px"><h3>About Us</h3>Our Story<br>Gift Wrap<br>Jewellery Care<br>Engraving</div>
  <div class="abs footer-col" style="left:973px"><h3>Shopping Online</h3>Contact Us<br>Australia Delivery<br>International Delivery<br>Returns</div>
  <div class="abs copyright">© 2018 Quillstone Jewellers Australia</div>
</footer>

</body>
</html>
```